An KADORI MIRETSU certified teacher needs a Business Card Design.

I need a business card to introduce and promote myself as an KADORI MIRETSU certified teacher and florist for fresh floral decoration services of venues ranging from executive rooms to large business and social events. I would prefer sober card with coloured avatar or vector image of a simple KADORI MIRETSU arrangement that has clear floral impression on the business card with my face book, and website address and other contact details like skype, cell and landlines, etc.
I have Teachers Fourth Grade Diploma, and Teaching Membership of Miretsu Mentors Guild (MMG), Japan.

Target Market(s)

Hospitality industry (Hotels, Cafes, Residency), Business organisations (executive rooms, meeting areas, conferences), Individuals & families (parties, social events), Hospitals and Clinics, etc.

Industry/Entity Type

Teacher

Contact Information for Business Card

Nazneen Bilqees
Certified Teacher, Miretsu Academy of Kadori
Cell: +92 317 604 5192
email: petalworx.pk@bloomvia.example
Facebook: http://www.socialpage.example/petalworx.pk
Website: www.petalworx.example

Requirements
Nice to have
• Avatar or vector of a classic/basic KADORI MIRETSU arrangement with vivid colour flowers
Should not have
• images of living things like women, etc.

```html
<!DOCTYPE html>
<html lang="en">
<head>
<meta charset="utf-8">
<title>Nazneen Bilqees — Business Card</title>
<link rel="stylesheet" href="https://fonts.googleapis.com/css2?family=Cabin:wght@400;600;700&display=swap">
<style>
  :root {
    --page-bg: #ece9e3;
    --card-white: #ffffff;
    --band-sage: #dfe0d2;
    --band-pink: #f6d9cf;
    --band-green: #8bb356;
    --ink: #111111;
    --icon-blue: #4a63b0;
  }
  * { box-sizing: border-box; margin: 0; padding: 0; }
  html, body { width: 1200px; height: 1000px; overflow: hidden; }
  body {
    background: var(--page-bg);
    font-family: "Cabin", "Gill Sans", sans-serif;
    color: var(--ink);
    position: relative;
  }
  .business-card {
    position: absolute;
    left: 100px; top: 215px;
    width: 1000px; height: 570px;
    background: var(--card-white);
    box-shadow: 0 10px 30px rgba(0,0,0,.18);
    overflow: hidden;
  }
  .floral-band {
    position: absolute; left: 0; width: 100%;
  }
  .floral-band--top {
    top: 0; height: 80px;
    background: linear-gradient(90deg, var(--band-sage) 0%, var(--band-sage) 55%, var(--band-pink) 80%, var(--band-sage) 100%);
  }
  .floral-band--bottom {
    bottom: 0; height: 110px;
    background: linear-gradient(90deg, var(--band-sage) 0%, #ecd5cb 45%, var(--band-sage) 70%, #c9d6ae 100%);
  }
  .card-body {
    position: absolute; top: 80px; bottom: 110px; left: 0; right: 0;
    display: flex; flex-direction: column; align-items: center;
    padding-top: 26px; text-align: center;
  }
  .holder-name {
    font-size: 44px; font-weight: 400; letter-spacing: 1px;
    text-shadow: 1px 2px 2px rgba(0,0,0,.3);
    line-height: 1;
  }
  .holder-title { font-size: 23px; font-weight: 700; margin-top: 12px; letter-spacing: .3px; }
  .holder-membership { font-size: 16px; line-height: 1.45; margin-top: 6px; }
  .contact-list { list-style: none; margin-top: 26px; font-size: 23px; line-height: 1.2; }
  .contact-item { display: flex; align-items: center; justify-content: center; gap: 14px; margin-bottom: 7px; }
  .contact-icon { width: 28px; height: 28px; flex: none; }
</style>
</head>
<body>
  <article class="business-card">
    <div class="floral-band floral-band--top" role="img" aria-label="Pastel floral pattern of leaves and blossoms"></div>

    <div class="card-body">
      <h1 class="holder-name">NAZNEEN BILQEES</h1>
      <p class="holder-title">Artist &amp; Teacher of Miretsu Academy of Kadori</p>
      <p class="holder-membership">Member, Miretsu Mentors Guild, Japan<br>Member, Karachi Chapter, Kadori Global Circle</p>

      <ul class="contact-list">
        <li class="contact-item">
          <svg class="contact-icon" viewBox="0 0 28 28" aria-hidden="true">
            <circle cx="14" cy="14" r="14" fill="var(--icon-blue)"/>
            <path d="M10 8c1 0 2 2.5 2 3s-1 1-1 1.5 2 3.5 3.5 3.5c.5 0 1-1 1.5-1s3 1 3 2-1.5 2-2.5 2C12 19 9 14 9 10c0-1 .5-2 1-2z" fill="#fff"/>
          </svg>
          <span>+92 317 604 5192</span>
        </li>
        <li class="contact-item">
          <svg class="contact-icon" viewBox="0 0 28 28" aria-hidden="true">
            <circle cx="14" cy="14" r="14" fill="var(--icon-blue)"/>
            <rect x="7.5" y="9.5" width="13" height="9" fill="#fff"/>
            <path d="M7.5 9.5 14 15l6.5-5.5" fill="none" stroke="var(--icon-blue)" stroke-width="1.3"/>
          </svg>
          <span>petalworx.pk@bloomvia.example</span>
        </li>
        <li class="contact-item">
          <svg class="contact-icon" viewBox="0 0 28 28" aria-hidden="true">
            <circle cx="14" cy="14" r="14" fill="var(--icon-blue)"/>
          </svg>
          <span>http://www.socialpage.example/petalworx.pk</span>
        </li>
        <li class="contact-item">
          <svg class="contact-icon" viewBox="0 0 28 28" aria-hidden="true">
            <circle cx="14" cy="14" r="14" fill="var(--icon-blue)"/>
            <g fill="none" stroke="#fff" stroke-width="1.4">
              <circle cx="14" cy="14" r="7"/>
              <ellipse cx="14" cy="14" rx="3" ry="7"/>
              <path d="M7 14h14"/>
            </g>
          </svg>
          <span>www.petalworx.example</span>
        </li>
      </ul>
    </div>

    <div class="floral-band floral-band--bottom" role="img" aria-label="Pastel floral pattern of stems, leaves and pink blossoms"></div>
  </article>
</body>
</html>
```